I want a business card that is going to show a creative spark but without limiting me to an industry. Something edgy but that wont go out of date. I want it state My business name Verity Lanes, profession - Professional Makeup Artist contact number and email

My service is to provide makeup services from bridal, fashion, photography, film, TV and so on. It is creative and different so i want that to be reflected.

I would like the card double sided.
Updates

 I would LOVE a background on my card something like this image... i can supply an image to be formed like this

Please use the image uploaded

Can we try using the image provided on one side of the card and then writing and details on the other side

Target Market(s)

I am targeting a wide range of people from Creative directors to the individual eg. bride

Industry/Entity Type

Business

Requirements
Must have
• Name: Harriet Cole
contact numbe 0417 583 940
email address:info@veritylanes.example
website: www.veritylanes.example
One of the images attached

professional makeup artist / hair stylist

I want it to show creativity
Nice to have
• logo, Double-sided card
Should not have
• the design should not use tradional style. Or images that are not my own

```html
<!DOCTYPE html>
<html lang="en">
<head>
<meta charset="UTF-8">
<title>Verity Lanes – Business Card</title>
<link rel="stylesheet" href="https://fonts.googleapis.com/css2?family=Kaushan+Script&family=Jost:ital,wght@0,400;0,500;1,400;1,500&display=swap">
<style>
  :root {
    --page: #ffffff;
    --card-edge: #8f8f8f;
    --front-light: #fbfbfb;
    --front-mist: #e6e8e6;
    --accent-red: #b3121f;
    --ink: #1e1e1e;
    --green-deep: #5f8f45;
    --green-mid: #79a85c;
    --green-light: #9cc283;
    --art-cream: #ecebdc;
    --art-olive: #c9cbb4;
    --art-rose: #e9c9c9;
    --white: #ffffff;
  }

  html, body {
    margin: 0;
    padding: 0;
    width: 1200px;
    height: 900px;
    overflow: hidden;
    background: var(--page);
  }

  .canvas {
    position: relative;
    width: 1200px;
    height: 900px;
  }

  .card {
    position: absolute;
    left: 304px;
    width: 678px;
    box-sizing: border-box;
    border: 1px solid var(--card-edge);
    overflow: hidden;
  }

  /* Front side */
  .card--front {
    top: 56px;
    height: 380px;
    background:
      radial-gradient(ellipse at 30% 40%, var(--front-light) 0%, transparent 60%),
      radial-gradient(ellipse at 80% 70%, var(--front-mist) 0%, transparent 55%),
      linear-gradient(135deg, var(--front-light) 0%, var(--front-mist) 100%);
  }

  .artwork {
    position: absolute;
    left: 8px;
    top: 14px;
    width: 330px;
    height: 350px;
    background: linear-gradient(160deg, var(--art-olive) 0%, var(--art-cream) 50%, var(--art-rose) 100%);
    opacity: 0.75;
  }

  .front-details {
    position: absolute;
    right: 26px;
    top: 236px;
    text-align: right;
  }

  .brand-name {
    font-family: "Kaushan Script", cursive;
    font-weight: 400;
    line-height: 1;
    margin: 0;
  }

  .profession {
    font-family: "Jost", sans-serif;
    font-style: italic;
    font-weight: 500;
    margin: 0;
  }

  .front-details .brand-name {
    font-size: 30px;
    color: var(--accent-red);
  }

  .front-details .profession {
    font-size: 14px;
    color: var(--ink);
    margin-top: 2px;
  }

  .contact {
    position: absolute;
    right: 26px;
    top: 332px;
    margin: 0;
    text-align: right;
    font-family: "Jost", sans-serif;
    font-size: 17px;
    color: var(--ink);
    line-height: 24px;
  }

  .contact .label {
    color: var(--accent-red);
    font-weight: 500;
  }

  /* Back side */
  .card--back {
    top: 456px;
    height: 376px;
    background:
      radial-gradient(ellipse at 20% 20%, var(--green-light) 0%, transparent 45%),
      radial-gradient(ellipse at 85% 75%, var(--green-deep) 0%, transparent 55%),
      linear-gradient(160deg, var(--green-mid) 0%, var(--green-deep) 100%);
  }

  .brand-disc {
    position: absolute;
    left: 256px;
    top: 42px;
    width: 188px;
    height: 188px;
    border-radius: 50%;
    background: var(--white);
  }

  .back-details {
    position: absolute;
    left: 0;
    right: 0;
    top: 256px;
    text-align: center;
    color: var(--white);
  }

  .back-details .brand-name {
    font-size: 40px;
  }

  .back-details .profession {
    font-size: 19px;
    margin-top: 2px;
  }
</style>
</head>
<body>
<main class="canvas">

  <section class="card card--front" aria-label="Card front">
    <div class="artwork" role="img" aria-label="Painted makeup illustration of an eye with green shadow and red lips"></div>

    <div class="front-details">
      <h1 class="brand-name">Verity Lanes</h1>
      <p class="profession">Professional Makeup Artist</p>
    </div>

    <address class="contact">
      <div><span class="label">m:</span> 0417 583 940</div>
      <div><span class="label">e:</span> info@veritylanes.example</div>
      <div><span class="label">w:</span> www.veritylanes.example</div>
    </address>
  </section>

  <section class="card card--back" aria-label="Card back">
    <div class="brand-disc" aria-hidden="true"></div>
    <div class="back-details">
      <h2 class="brand-name">Verity Lanes</h2>
      <p class="profession">Professional Makeup Artist</p>
    </div>
  </section>

</main>
</body>
</html>
```